Rural contractor needs professional informative business card

We need a business card design that looks professional but also includes information about the services that the business offers.
The business is an earthmoving and transport business. All of the services offered are listed on the old card attached.
The business is aimed at farmers so the design we are after is a classic look. The card needs to include all of the information that is listed on the old card design uploaded as an attachment. We recognize that this is a lot of information to fit on a business card but it also operates as a key marketing tool so is very important to the business.
Feel free to send me your questions.
Thanks
Reason: We are having trouble deciding between all these great designs - thank you for your efforts
We would love to see some designs using red with a little white and black. Also feel free to re-design our logo if you feel it needs to be to fit your designs. Thank you

```html
<!DOCTYPE html>
<html lang="en">
<head>
<meta charset="utf-8">
<title>RT Hallett Contracting – Business Card</title>
<link href="https://fonts.googleapis.com/css2?family=Montserrat:ital,wght@0,400;0,500;0,600;1,400&display=swap" rel="stylesheet">
<style>
  :root {
    --stage: #e4e6e5;
    --ink: #1f1f1f;
    --band: #2e2e2e;
    --strip: #8f8f8c;
    --paper-light: #e9e9e7;
    --paper-mid: #cfcfcc;
    --photo-a: #9aa3ab;
    --photo-b: #a9a296;
    --white: #ffffff;
    --muted: #d8d8d8;
  }
  * { box-sizing: border-box; margin: 0; padding: 0; }
  html, body { width: 1200px; height: 900px; overflow: hidden; }
  body {
    background: var(--stage);
    font-family: "Montserrat", Arial, sans-serif;
    position: relative;
  }
  .card {
    position: absolute;
    left: 270px;
    width: 660px;
    height: 402px;
    overflow: hidden;
    box-shadow: 0 6px 18px rgba(0,0,0,.18);
  }
  .card--front { top: 30px; background: var(--paper-light); }
  .card--back { top: 468px; background: var(--band); }

  /* Front */
  .front-photo {
    position: absolute; inset: 0;
    background: linear-gradient(180deg, var(--paper-light) 0%, #dcdcd9 45%, var(--paper-mid) 100%);
  }
  .brand {
    position: absolute; left: 40px; top: 44px;
    color: var(--ink);
    font-weight: 600;
  }
  .brand__name { font-size: 44px; letter-spacing: 0.5px; line-height: 1; }
  .brand__sub { font-size: 17px; letter-spacing: 11px; margin-top: 12px; }
  .holder {
    position: absolute; left: 34px; top: 200px;
    font-size: 23px; font-weight: 600; letter-spacing: 2px; color: var(--ink);
  }
  .front-band {
    position: absolute; left: 0; right: 0; top: 238px; height: 112px;
    background: var(--band); color: var(--muted);
    padding: 14px 34px 0;
  }
  .contact { font-size: 15px; letter-spacing: 1.4px; line-height: 1.45; }
  .contact__rule { width: 470px; height: 1px; background: var(--muted); margin: 4px 0 8px; }
  .tagline { font-size: 15px; font-style: italic; letter-spacing: 2.6px; }
  .front-strip {
    position: absolute; left: 0; right: 0; top: 350px; bottom: 0;
    background: var(--strip);
  }

  /* Back */
  .back-photo {
    position: absolute; left: 0; right: 0; top: 0; height: 208px;
    background: linear-gradient(135deg, var(--photo-a) 0%, var(--photo-b) 100%);
  }
  .services {
    position: absolute; color: var(--white);
    font-size: 16px; font-weight: 500; letter-spacing: 1.6px;
  }
  .services--earth { left: 40px; top: 262px; }
  .services--transport { left: 466px; top: 222px; }
  .services__title { font-size: 16px; font-weight: 500; letter-spacing: 2px; margin-bottom: 4px; }
  .services__list { list-style: none; }
  .services__list li { display: flex; align-items: center; gap: 10px; line-height: 1.55; }
  .tick { width: 14px; height: 12px; flex: none; }
</style>
</head>
<body>

<section class="card card--front" aria-label="Card front">
  <div class="front-photo" role="img" aria-label="Faded photo of a prime mover hauling cotton modules"></div>
  <div class="brand">
    <div class="brand__name">RT Hallett</div>
    <div class="brand__sub">CONTRACTING</div>
  </div>
  <div class="holder">Rowan Hallett</div>
  <div class="front-band">
    <p class="contact">42 Tarcoola Street, Westvale 2830<br>P: 0400 123 456 | E: rowanhallett@mailpost.com</p>
    <div class="contact__rule"></div>
    <p class="tagline">Earthmoving &amp; Transport Solutions</p>
  </div>
  <div class="front-strip"></div>
</section>

<section class="card card--back" aria-label="Card back">
  <div class="back-photo" role="img" aria-label="Photo of a prime mover with flat-top trailers in a yard"></div>

  <div class="services services--earth">
    <h3 class="services__title">EARTHMOVING</h3>
    <ul class="services__list">
      <li><svg class="tick" viewBox="0 0 14 12"><path d="M1 6.5 5 10.5 13 1.5" fill="none" stroke="#fff" stroke-width="2.4"/></svg>Road Building &amp; Maintenance</li>
      <li><svg class="tick" viewBox="0 0 14 12"><path d="M1 6.5 5 10.5 13 1.5" fill="none" stroke="#fff" stroke-width="2.4"/></svg>Poly Pipe Laying</li>
      <li><svg class="tick" viewBox="0 0 14 12"><path d="M1 6.5 5 10.5 13 1.5" fill="none" stroke="#fff" stroke-width="2.4"/></svg>Clearing Fence Lines</li>
      <li><svg class="tick" viewBox="0 0 14 12"><path d="M1 6.5 5 10.5 13 1.5" fill="none" stroke="#fff" stroke-width="2.4"/></svg>Sand &amp; Gravel Supplies</li>
    </ul>
  </div>

  <div class="services services--transport">
    <h3 class="services__title">TRANSPORT</h3>
    <ul class="services__list">
      <li><svg class="tick" viewBox="0 0 14 12"><path d="M1 6.5 5 10.5 13 1.5" fill="none" stroke="#fff" stroke-width="2.4"/></svg>Grain</li>
      <li><svg class="tick" viewBox="0 0 14 12"><path d="M1 6.5 5 10.5 13 1.5" fill="none" stroke="#fff" stroke-width="2.4"/></svg>Cotton</li>
      <li><svg class="tick" viewBox="0 0 14 12"><path d="M1 6.5 5 10.5 13 1.5" fill="none" stroke="#fff" stroke-width="2.4"/></svg>Sand &amp; Gravel</li>
      <li><svg class="tick" viewBox="0 0 14 12"><path d="M1 6.5 5 10.5 13 1.5" fill="none" stroke="#fff" stroke-width="2.4"/></svg>Wool</li>
    </ul>
  </div>
</section>

</body>
</html>
```